Beauty Page

**UPDATED Brief**
We are looking for a website for a beauty organisation that targets both MEN & WOMAN. The focus of the company is in four main areas:

- Health
* Naturopathy & Remedial Massage
- Body
* Yoga
* Personal Training
* Massage
- Skin
* Skin care products such as Velmoracine
- Beauty
* Waxing
* Eye Treatments

We have attached the logo, (a sample of the website that I did - based on the book) and the sample of the pdf book
Updates

Dear All,

Thank you for your patience regarding the beauty contest. We were not happy with the designs that were submitted to us. We therefore had the Graphic designer to do the pricelist book to get all the colours for the organisation.

We are now happy to relaunch the contest and invite you all to take a look at the brief, download a sample of the book and the website we designed on what I’m looking for (the website is only a draft so I don’t want you to copy it) and let your creative mind go wild and present some suggestions to us.

Thanks

 

Target Market(s)

Woman & Men age 24 - 60

Industry/Entity Type

It Company

Requirements
Must have
• Use of main colours
Black
White
Gray - (CYMK - 65, 58, 57, 37)
Purpleish - Maroon (CYMK - 52, 69, 47, 25)

Use of the three color dots on the page.
(white, maroon & Gray)
Same fonts as the book
- Helvetica LT Std
Should not have
• Logo must not be altered i.e different colours, fonts, shadows etc...

```html
<!DOCTYPE html>
<html lang="en">
<head>
<meta charset="utf-8">
<title>Lumentra &amp; Beauty</title>
<link rel="stylesheet" href="https://fonts.googleapis.com/css2?family=Roboto+Condensed:wght@300;400;700&family=Arimo:wght@400&display=swap">
<style>
:root{
  --maroon:#7b1d50;
  --maroon-deep:#5c0e39;
  --maroon-light:#9a3a6d;
  --ink:#1d1d1d;
  --grey:#6b6b6b;
  --line:#e2e2e2;
  --panel:#ffffff;
  --page:#ffffff;
  --ribbon:#b9dbe9;
  --lime:#b5cc1c;
}
*{box-sizing:border-box;margin:0;padding:0}
html,body{width:993px;height:1200px;overflow:hidden;background:var(--page)}
body{font-family:"Roboto Condensed",Arial,sans-serif;color:var(--ink);position:relative}
.abs{position:absolute}
.page-frame{position:absolute;left:19px;top:22px;width:954px;height:1164px;border:1px solid #dcdcdc;background:var(--page)}
.page-top-shade{left:20px;top:23px;width:952px;height:460px;background:linear-gradient(#fafafa,#f3f3f3 80%,#fff)}

.site-header{left:68px;top:66px;width:857px;height:91px;background:linear-gradient(#fff,#f4f4f4);box-shadow:0 1px 3px rgba(0,0,0,.12)}
.brand{left:22px;top:20px;display:flex;align-items:center;gap:8px;font-weight:700;font-size:32px;color:var(--ink)}
.brand-dot{width:12px;height:12px;background:var(--maroon)}

.main-nav{left:68px;top:158px;width:857px;height:33px;background:linear-gradient(var(--maroon-light),var(--maroon-deep));display:flex;justify-content:flex-end;box-shadow:0 2px 3px rgba(0,0,0,.2)}
.main-nav a{color:#fff;text-decoration:none;font-weight:700;font-size:15px;line-height:33px;padding:0 18px;border-left:1px solid rgba(0,0,0,.25)}
.main-nav a:first-child{border-left:none}

.hero{left:74px;top:199px;width:849px;height:270px;background:var(--panel);border:1px solid #e4e4e4;box-shadow:0 6px 6px -4px rgba(0,0,0,.35)}
.hero-photo{left:544px;top:0;width:304px;height:268px;background:radial-gradient(ellipse at 55% 45%,#f2d5c3 0,#ecd0c0 30%,#f7f2ee 60%,#fff 85%)}
.hero-title{left:60px;top:42px;width:470px;font-weight:700;font-size:38px;line-height:44px;color:var(--maroon);letter-spacing:-.8px;z-index:1}
.hero-title strong{color:var(--maroon-deep)}
.hero-text{left:60px;top:143px;font-size:17px;line-height:22px;color:var(--maroon)}
.button{background:var(--maroon);color:#fff;font-size:16px;padding:4px 8px;text-decoration:none}
.hero-button{left:61px;top:205px}
.slide-arrow{width:15px;height:33px;background:var(--maroon-deep);display:flex;align-items:center;justify-content:center}
.hero .arrow-prev{left:-8px;top:100px}
.hero .arrow-next{right:-8px;top:100px}

.welcome-title{left:0;width:993px;top:516px;text-align:center;font-weight:700;font-size:35px;color:var(--maroon-deep)}
.welcome-text{left:96px;width:801px;top:568px;text-align:center;font-size:16.5px;line-height:27px;color:var(--grey);font-weight:300}

.feature-card{top:653px;width:272px;height:180px;background:var(--panel);border:1px solid #dedede;box-shadow:0 4px 4px -3px rgba(0,0,0,.25)}
.card-bar{left:-1px;bottom:-1px;width:272px;height:37px;background:linear-gradient(var(--maroon-light),var(--maroon-deep));color:#fff;font-weight:700;font-size:18px;line-height:37px;padding-left:27px}
.card-bar svg{position:absolute;right:14px;top:10px}
.partner-name{left:14px;top:60px;font-size:24px;font-weight:400;color:var(--grey);display:flex;align-items:center;gap:8px}
.partner-mark{width:20px;height:20px;border-radius:50%;background:var(--grey)}
.stones-photo{left:80px;top:12px;width:110px;height:120px;background:radial-gradient(ellipse at 50% 60%,#2a2a2a 0,#3d3d3d 35%,#e8efe0 62%,#fff 75%)}
.ribbon{left:0;top:0}
.promo-title{right:10px;top:8px;font-weight:700;font-size:20px;color:var(--maroon-deep);text-align:right}
.promo-sub{right:10px;top:33px;font-size:15px;color:var(--maroon);text-align:right}
.range-brand{left:10px;top:74px;width:250px;font-size:24px;color:var(--grey);text-align:center;font-weight:400}

.section-rule{left:77px;top:858px;width:850px;height:1px;background:var(--line)}

.newsletter{left:77px;top:889px;width:272px;height:202px;background:var(--panel);border:1px solid #dedede}
.newsletter-photo{left:0;top:30px;width:140px;height:135px;background:radial-gradient(ellipse at 45% 60%,#dfe9d8 0,#cfdcc6 35%,#eef2ee 65%,#fff 85%)}
.newsletter .promo-sub{line-height:19px;top:35px}
.newsletter-button{left:171px;top:122px}

.product-slide{left:377px;top:891px;width:543px;height:199px;background:var(--panel);border:1px solid #e2e2e2;box-shadow:0 6px 6px -4px rgba(0,0,0,.3)}
.product-title{left:28px;top:24px;font-family:"Arimo",Arial,sans-serif;font-size:31px;color:var(--lime);letter-spacing:-.5px}
.product-title sup{font-size:10px}
.product-text{left:30px;top:76px;width:300px;text-align:center;font-size:17px;line-height:22px;color:var(--grey);font-weight:300}
.product-photo{left:358px;top:26px;width:156px;height:142px;background:linear-gradient(90deg,#d9d9d9,#f4f4f4 30%,#cfcfcf 55%,#f0f0f0 80%,#dadada)}
.product-slide .slide-arrow{height:28px;width:14px}
.product-slide .arrow-prev{left:-2px;top:82px}
.product-slide .arrow-next{right:-2px;top:82px}

.site-footer-connect{left:79px;top:1133px;display:flex;align-items:center;gap:14px;font-weight:700;font-size:18px;color:var(--maroon)}
.social-circle{width:28px;height:28px;border-radius:50%;background:linear-gradient(#fff,#e2e2e2);box-shadow:0 1px 2px rgba(0,0,0,.3)}
.legal-links{right:78px;top:1136px;font-family:"Arimo",Arial,sans-serif;font-size:12px;color:var(--grey);display:flex;gap:10px}
.legal-links span+span{border-left:1px solid #ccc;padding-left:10px}
</style>
</head>
<body>
<div class="page-frame"></div>
<div class="page-top-shade abs"></div>

<header class="site-header abs">
  <div class="brand abs"><span>Lumentra &amp; Beauty</span><span class="brand-dot"></span></div>
</header>

<nav class="main-nav abs">
  <a href="#">HOME</a><a href="#">ABOUT US</a><a href="#">SERVICES &amp; TREATMENT</a><a href="#">CONTACT US</a>
</nav>

<section class="hero abs">
  <div class="hero-photo abs" role="img" aria-label="Woman in a white towel holding a white calla lily"></div>
  <h1 class="hero-title abs">HELPING YOU TO <strong>LOVE YOUR</strong><br>SKIN AND <strong>FEEL GOOD</strong></h1>
  <p class="hero-text abs">Through our treatments, products and education we aim<br>to give you total body wellbeing.</p>
  <a class="button hero-button abs" href="#">Find our more</a>
  <span class="slide-arrow arrow-prev abs"><svg width="7" height="11"><path d="M6 1 2 5.5 6 10" stroke="#fff" stroke-width="2.4" fill="none"/></svg></span>
  <span class="slide-arrow arrow-next abs"><svg width="7" height="11"><path d="M1 1 5 5.5 1 10" stroke="#fff" stroke-width="2.4" fill="none"/></svg></span>
</section>

<h2 class="welcome-title abs">WELCOME TO LUMENTRA &amp; BEAUTY</h2>
<p class="welcome-text abs">We are a family established health, massage, skincare centre that provides quality professional treatments and<br>education to each and every client. We pride oursleves on being able to cater for all individuals.</p>

<article class="feature-card abs" style="left:77px">
  <div class="partner-name abs"><span class="partner-mark"></span><span>Silverline Guild</span></div>
  <a class="card-bar abs">ABOUT US<svg width="10" height="16"><path d="M2 2 8 8 2 14" stroke="#fff" stroke-width="3" fill="none"/></svg></a>
</article>

<article class="feature-card abs" style="left:365px">
  <div class="stones-photo abs" role="img" aria-label="Stacked black massage stones with a green leaf"></div>
  <a class="card-bar abs">SERVICES &amp; TREATMENTS<svg width="10" height="16"><path d="M2 2 8 8 2 14" stroke="#fff" stroke-width="3" fill="none"/></svg></a>
</article>

<article class="feature-card abs" style="left:655px">
  <svg class="ribbon abs" width="72" height="72"><path d="M0 0H72L0 72Z" fill="var(--ribbon)"/><text x="14" y="38" transform="rotate(-45 22 30)" fill="#fff" font-family="Roboto Condensed" font-weight="700" font-size="14">NEW</text></svg>
  <div class="promo-title abs">Correct and repair</div>
  <div class="promo-sub abs">skin range available now!</div>
  <div class="range-brand abs">Maison Coralie</div>
  <a class="card-bar abs">PRODUCT RANGES<svg width="10" height="16"><path d="M2 2 8 8 2 14" stroke="#fff" stroke-width="3" fill="none"/></svg></a>
</article>

<div class="section-rule abs"></div>

<article class="newsletter abs">
  <div class="newsletter-photo abs" role="img" aria-label="Skincare bottles beside a bowl of cream and green leaves"></div>
  <svg class="ribbon abs" width="72" height="72"><path d="M0 0H72L0 72Z" fill="var(--ribbon)"/><text x="14" y="38" transform="rotate(-45 22 30)" fill="#fff" font-family="Roboto Condensed" font-weight="700" font-size="14">NEW</text></svg>
  <div class="promo-title abs">Keep up todate</div>
  <div class="promo-sub abs">News &amp; offers<br>available now!</div>
  <a class="button newsletter-button abs" href="#">Download</a>
  <a class="card-bar abs">NEWSLETTER<svg width="10" height="16"><path d="M2 2 8 8 2 14" stroke="#fff" stroke-width="3" fill="none"/></svg></a>
</article>

<section class="product-slide abs">
  <div class="product-title abs">ClearaDerm Balance<sup>TM</sup></div>
  <p class="product-text abs">A 24 - hour treatment system that uses the state-of-the-art technology to tackle adult breakouts. Each product is designed to be layered for maximum effectiveness.</p>
  <div class="product-photo abs" role="img" aria-label="Row of Velmoracine skincare bottles and tubes"></div>
  <span class="slide-arrow arrow-prev abs"><svg width="7" height="11"><path d="M6 1 2 5.5 6 10" stroke="#fff" stroke-width="2.4" fill="none"/></svg></span>
  <span class="slide-arrow arrow-next abs"><svg width="7" height="11"><path d="M1 1 5 5.5 1 10" stroke="#fff" stroke-width="2.4" fill="none"/></svg></span>
</section>

<footer>
  <div class="site-footer-connect abs"><span>CONNECT WITH US!</span><span class="social-circle" aria-label="Social page"></span></div>
  <div class="legal-links abs"><span>Privacy Policy</span><span>Terms of use</span></div>
</footer>
</body>
</html>
```